New Business Card Design Project

Looking for a modern business card design for an import distribution business for industrial technical products. The winning design will translate modern, sophistication, technical, professional and sustainable.

Target Market(s)

Technical customers

Industry/Entity Type

Business

Contact Information for Business Card

Dean Harlow
Sales Manager
M: 0471 625 183
P: 1300 872 619
dean@volkarsystems.com.au
4/18 Galloway Crest Road
Brenton Vale NSW 2163
www.volkarsystems.com.au

Font styles to use
Sans Serif

Colors
ec1f27
606060
000000
fbfbfb

Requirements
Must have
• My Logo which is the Volkar Systems logo attached
Nice to have
• Eurostile Bold font

```html
<!DOCTYPE html>
<html lang="en">
<head>
<meta charset="utf-8">
<title>Volkar Systems – Business Card</title>
<link rel="stylesheet" href="https://fonts.googleapis.com/css2?family=Saira:wght@500;600;700&display=swap">
<style>
  :root {
    --brand-red: #d52b26;
    --brand-grey: #606469;
    --ink: #111111;
    --card-paper: #efefef;
    --tint: #f1dfd4;
    --tint-grey: #e2e2e2;
    --backdrop: #2b2b2b;
  }
  html, body {
    margin: 0;
    width: 1200px;
    height: 800px;
    overflow: hidden;
    background: var(--backdrop);
  }
  .sheet {
    position: relative;
    width: 1200px;
    height: 800px;
    display: flex;
    align-items: center;
    justify-content: center;
    gap: 28px;
  }
  .card {
    display: block;
    width: 540px;
    height: 308px;
    box-shadow: 0 6px 14px rgba(0,0,0,0.55);
    font-family: "Saira", sans-serif;
  }
  .card-paper { fill: var(--card-paper); }
  .band-red { fill: var(--brand-red); }
  .band-grey { fill: var(--brand-grey); }
  .band-divider { fill: none; stroke: #ffffff; stroke-width: 3; }
  .tint-block { fill: var(--tint); }
  .tint-block-grey { fill: var(--tint-grey); }
  .brand-square { fill: var(--brand-red); }
  .brand-name { fill: var(--brand-red); font-weight: 700; letter-spacing: 1px; }
  .person-name { fill: var(--brand-red); font-weight: 600; font-size: 29px; }
  .person-title { fill: var(--ink); font-weight: 500; font-size: 19px; }
  .rule { stroke: var(--ink); stroke-width: 1.2; }
  .contact { fill: var(--ink); font-weight: 500; font-size: 17px; }
  .contact-small { font-size: 15.5px; }
  .icon-bg { fill: var(--brand-red); }
  .icon-mark { fill: none; stroke: #ffffff; stroke-width: 1.4; stroke-linecap: round; stroke-linejoin: round; }
  .icon-fill { fill: #ffffff; }
</style>
</head>
<body>
<main class="sheet">

  <!-- Front of card -->
  <svg class="card card-front" viewBox="0 0 670 382" role="img" aria-label="Volkar Systems business card, front">
    <rect class="card-paper" width="670" height="382"/>

    <rect class="tint-block" x="247" y="138" width="170" height="170" opacity="0.75"/>

    <g class="brand">
      <rect class="brand-square" x="43" y="47" width="60" height="60"/>
      <text class="brand-name" x="120" y="93" font-size="44">VOLKAR SYSTEMS</text>
    </g>

    <line class="rule" x1="32" y1="191" x2="486" y2="191"/>
    <text class="person-name" x="638" y="173" text-anchor="end">Dean Harlow</text>
    <text class="person-title" x="636" y="197" text-anchor="end">Sales Manager</text>

    <g class="contact-list">
      <g class="contact-row">
        <rect class="icon-bg" x="33" y="216" width="14" height="13" rx="1.5"/>
        <path class="icon-mark" d="M36 221 q4 -3 8 0 M37 226 h6 v-3 h-6 z"/>
        <text class="contact" x="60" y="229">0471 625 183</text>
      </g>
      <g class="contact-row">
        <rect class="icon-bg" x="33" y="241" width="14" height="14" rx="1.5"/>
        <rect class="icon-mark" x="37.5" y="243.5" width="5" height="9" rx="1"/>
        <text class="contact" x="60" y="254">1300 872 619</text>
      </g>
      <g class="contact-row">
        <rect class="icon-bg" x="33" y="266" width="14" height="14" rx="1.5"/>
        <circle class="icon-mark" cx="40" cy="273" r="4.5"/>
        <path class="icon-mark" d="M35.5 273 h9 M40 268.5 v9"/>
        <text class="contact contact-small" x="60" y="279">www.volkarsystems.com.au</text>
      </g>
      <g class="contact-row">
        <rect class="icon-bg" x="33" y="291" width="14" height="13" rx="1.5"/>
        <path class="icon-mark" d="M35.5 294.5 h9 v7 h-9 z M35.5 294.5 l4.5 4 l4.5 -4"/>
        <text class="contact contact-small" x="60" y="304">dean@volkarsystems.com.au</text>
      </g>
    </g>

    <g class="address">
      <text class="contact contact-small" x="613" y="280" text-anchor="end">4/18 Galloway Crest Road</text>
      <text class="contact contact-small" x="613" y="303" text-anchor="end">Brenton Vale NSW 2163</text>
      <rect class="icon-bg" x="622" y="267" width="14" height="14" rx="1.5"/>
      <path class="icon-fill" d="M629 278.5 l-3 -4.5 a3.4 3.4 0 1 1 6 0 z"/>
      <circle cx="629" cy="272.3" r="1.1" fill="var(--brand-red)"/>
    </g>

    <g class="footer-band">
      <rect class="band-red" x="0" y="333" width="670" height="49"/>
      <path class="band-grey" d="M0 341 H318 L346 382 H0 Z"/>
      <path class="band-divider" d="M0 339 H320 L349 382"/>
    </g>
  </svg>

  <!-- Back of card -->
  <svg class="card card-back" viewBox="0 0 670 382" role="img" aria-label="Volkar Systems business card, back">
    <rect class="card-paper" width="670" height="382"/>

    <rect class="tint-block" x="355" y="27" width="143" height="308" opacity="0.75"/>
    <rect class="tint-block-grey" x="524" y="27" width="146" height="143" opacity="0.8"/>
    <rect class="tint-block" x="524" y="196" width="146" height="139" opacity="0.75"/>

    <g class="brand">
      <rect class="brand-square" x="146" y="152" width="61" height="61"/>
      <text class="brand-name" x="224" y="199" font-size="44">VOLKAR SYSTEMS</text>
    </g>

    <g class="footer-band">
      <rect class="band-grey" x="0" y="335" width="670" height="47"/>
      <path class="band-red" d="M0 343 H316 L345 382 H0 Z"/>
      <path class="band-divider" d="M0 341 H318 L348 382"/>
    </g>
  </svg>

</main>
</body>
</html>
```